Bluegate Physiotherapy
Business Cards, Stationary, Letterhead, Magnet, Presentation Folder, A5 Referral Pad, Email Signatur
Bluegate Physiotherapy -
Creative Brief
Professional
Tom Ellingsworth
BSc Physiotherapy / Acupuncturist / Cert IV Occupational Health & Safety
Unit 3, 48 Kestrel Lane, Mandurah WA 6210
tom.ellingsworth@bluegatephysio-example.com.au
www.bluegatephysio-example.com.au
Magnet to be standard business card size (portrait OR landscape) and include only phone, address and website (in addition to graphic component). Referral pad to be A5 size. At the TOP: "Patient Name", "Date" as well as 4 tick boxes "W.C.", "Vet. Affairs", "Private" "EPC". At the BOTTOM: "Referring Doctor" "Sign" "Doctors Name" and "Address" as well as "Preferred Contact" with 4 tick boxes "E-mail", "Phone", "Fax", "Snail Mail". Down one SIDE to have a list: "Manual Therapy", "Massage", "Exercise Prescription", "Gym Based Rehab", "Workplace Assessment", "Ergonomics", "Acupuncture", "Sports Physiotherapy", "Womens Health".

```html
<!DOCTYPE html>
<html lang="en">
<head>
<meta charset="utf-8">
<title>Bluegate Physiotherapy – Stationery Suite</title>
<link href="https://fonts.googleapis.com/css2?family=Open+Sans:wght@400;700&display=swap" rel="stylesheet">
<style>
:root{
  --board:#7c4219;
  --board-dark:#5e2f10;
  --paper:#ffffff;
  --blue:#1a8fd6;
  --blue-light:#7cc8f2;
  --orange:#f39a1e;
  --green:#7cc242;
  --ink:#3a3a3a;
  --muted:#9a9a9a;
  --rule:#c9c9c9;
}
*{box-sizing:border-box;margin:0;padding:0}
html,body{width:1200px;height:583px;overflow:hidden}
body{background:radial-gradient(ellipse at 50% 40%,var(--board) 0%,var(--board-dark) 100%);font-family:"Open Sans",Arial,sans-serif;color:var(--ink);position:relative}
.item{position:absolute;background:var(--paper);box-shadow:0 2px 5px rgba(0,0,0,.45);overflow:hidden}
.brand{display:flex;align-items:center;gap:3px;font-weight:700;color:var(--blue);white-space:nowrap}
.brand .dot{border-radius:50%;background:var(--orange);flex:none}
.tiny{font-size:3.4px;line-height:1.35;color:var(--muted)}
.mark-area{position:absolute;background:radial-gradient(circle,rgba(26,143,214,.10),rgba(243,154,30,.06) 55%,transparent 70%)}
.wave{position:absolute;left:0;bottom:0;width:100%}
/* letterhead */
.letterhead{top:12px;width:151px;height:168px}
.letterhead .brand{position:absolute;left:10px;top:9px;font-size:5.5px}
.letterhead .brand .dot{width:6px;height:6px}
/* referral pad */
.pad{top:12px;width:144px;height:168px}
.pad .spiral{position:absolute;top:0;left:0;width:100%;height:6px;background:repeating-linear-gradient(90deg,#555 0 1.5px,transparent 1.5px 4px)}
.pad .head{position:absolute;top:6px;left:0;width:100%;height:28px;padding:5px 7px;display:flex;justify-content:space-between}
.pad .head .brand{font-size:5px}
.pad .head .brand .dot{width:5px;height:5px}
.pad.blue .head{background:linear-gradient(90deg,var(--blue),var(--blue-light))}
.pad.blue .head .brand,.pad.orange .head .brand{color:#fff}
.pad.grey .head{background:linear-gradient(90deg,#fff,#dcdcdc)}
.pad.orange .head{background:linear-gradient(90deg,var(--orange),#fcd27a)}
.pad .fields{position:absolute;top:38px;left:7px;right:7px}
.field{font-size:3.6px;color:var(--ink);border-bottom:.5px solid var(--rule);height:7px;margin-bottom:2px}
.ticks{display:flex;gap:5px;font-size:3.4px;margin:2px 0 4px}
.ticks span::before{content:"";display:inline-block;width:3px;height:3px;border:.5px solid var(--ink);margin-right:1px;vertical-align:middle}
.services{position:absolute;top:70px;right:7px;width:38px;font-size:3.3px;line-height:1.6;color:var(--blue);list-style:none}
.pad .bottom{position:absolute;bottom:8px;left:7px;width:88px}
/* cards */
.card{width:41px;height:18px}
.card .brand{position:absolute;left:3px;top:3px;font-size:3.6px}
.card .brand .dot{width:3px;height:3px}
.card.wide .brand{font-size:2.6px;gap:2px}
.card.wide .brand .dot{width:2.5px;height:2.5px}
.card .phone{position:absolute;left:3px;top:9px;font-size:2.8px;white-space:nowrap}
.card.orange{background:linear-gradient(135deg,var(--orange),#c8660c)}
.card.blue{background:linear-gradient(135deg,var(--blue-light),var(--blue))}
.card.green{background:linear-gradient(135deg,#b6e07d,var(--green))}
.card.dark{background:linear-gradient(135deg,#f7b24a,#7a3c0c)}
.card.orange .brand,.card.blue .brand,.card.green .brand,.card.dark .brand{color:#fff}
.card.orange .dot,.card.dark .dot{background:#fff}
/* folder */
.folder-cover{left:211px;top:206px;width:327px;height:180px;background:radial-gradient(ellipse at 40% 45%,#e8f5fd 0%,var(--blue-light) 45%,var(--blue) 100%)}
.folder-cover .brand{position:absolute;left:30px;top:14px;font-size:9px}
.folder-cover .brand .dot{width:9px;height:9px}
.folder-inside{left:552px;top:206px;width:365px;height:180px}
.pocket{position:absolute;right:0;bottom:0;width:185px;height:50px;background:linear-gradient(90deg,var(--blue-light),var(--blue))}
/* envelopes */
.envelope{left:941px;width:206px}
.envelope .brand{position:absolute;left:8px;top:8px;font-size:6px}
.envelope .brand .dot{width:6px;height:6px}
.envelope .contact{position:absolute;left:8px;top:18px;width:80px}
.envelope .flap{position:absolute;right:0;bottom:0;width:100%;height:14px}
</style>
</head>
<body>

<!-- letterheads -->
<section class="item letterhead" style="left:149px">
  <div class="brand"><span class="dot"></span>Bluegate Physiotherapy</div>
  <div class="mark-area" role="img" aria-label="Faint brand tree decoration" style="left:30px;top:45px;width:90px;height:80px"></div>
  <svg class="wave" viewBox="0 0 151 22" height="22" aria-hidden="true"><path d="M0 14 Q60 0 151 8 V22 H0Z" fill="var(--orange)"/><path d="M0 18 Q70 6 151 12 V22 H0Z" fill="var(--blue)"/></svg>
</section>
<section class="item letterhead" style="left:305px">
  <div class="brand"><span class="dot"></span>Bluegate Physiotherapy</div>
  <div class="mark-area" role="img" aria-label="Faint brand tree decoration" style="left:30px;top:45px;width:90px;height:80px"></div>
  <svg class="wave" viewBox="0 0 151 22" height="22" aria-hidden="true"><path d="M0 14 Q60 0 151 8 V22 H0Z" fill="var(--orange)"/><path d="M0 18 Q70 6 151 12 V22 H0Z" fill="var(--blue)"/></svg>
</section>

<!-- referral pads -->
<section class="item pad blue" style="left:463px">
  <div class="spiral"></div>
  <div class="head"><div class="brand"><span class="dot"></span>Bluegate Physiotherapy</div></div>
  <div class="fields">
    <div class="field">Patient Name</div><div class="field">Date</div>
    <div class="ticks"><span>W.C.</span><span>Vet. Affairs</span><span>Private</span><span>EPC</span></div>
  </div>
  <div class="mark-area" role="img" aria-label="Faint brand tree decoration" style="left:30px;top:70px;width:70px;height:60px"></div>
  <ul class="services"><li>Manual Therapy</li><li>Massage</li><li>Exercise Prescription</li><li>Gym Based Rehab</li><li>Workplace Assessment</li><li>Ergonomics</li><li>Acupuncture</li><li>Sports Physiotherapy</li><li>Womens Health</li></ul>
  <div class="bottom"><div class="field">Referring Doctor</div><div class="field">Sign</div><div class="field">Doctors Name</div><div class="field">Address</div>
  <div class="ticks"><span>E-mail</span><span>Phone</span><span>Fax</span><span>Snail Mail</span></div></div>
</section>
<section class="item pad grey" style="left:617px">
  <div class="spiral"></div>
  <div class="head"><div class="brand"><span class="dot"></span>Bluegate Physiotherapy</div><div class="tiny" style="width:42px">Unit 3, 48 Kestrel Lane, Mandurah WA 6210</div></div>
  <div class="fields">
    <div class="field">Patient Name</div><div class="field">Date</div>
    <div class="ticks"><span>W.C.</span><span>Vet. Affairs</span><span>Private</span><span>EPC</span></div>
  </div>
  <div class="mark-area" role="img" aria-label="Faint brand tree decoration" style="left:30px;top:70px;width:70px;height:60px"></div>
  <ul class="services"><li>Manual Therapy</li><li>Massage</li><li>Exercise Prescription</li><li>Gym Based Rehab</li><li>Workplace Assessment</li><li>Ergonomics</li><li>Acupuncture</li><li>Sports Physiotherapy</li><li>Womens Health</li></ul>
  <div class="bottom"><div class="field">Referring Doctor</div><div class="field">Sign</div><div class="field">Doctors Name</div><div class="field">Address</div>
  <div class="ticks"><span>E-mail</span><span>Phone</span><span>Fax</span><span>Snail Mail</span></div></div>
</section>
<section class="item pad orange" style="left:773px">
  <div class="spiral"></div>
  <div class="head"><div class="brand"><span class="dot" style="background:#fff"></span>Bluegate Physiotherapy</div></div>
  <div class="fields">
    <div class="field">Patient Name</div><div class="field">Date</div>
    <div class="ticks"><span>W.C.</span><span>Vet. Affairs</span><span>Private</span><span>EPC</span></div>
  </div>
  <div class="mark-area" role="img" aria-label="Faint brand tree decoration" style="left:30px;top:70px;width:70px;height:60px"></div>
  <ul class="services"><li>Manual Therapy</li><li>Massage</li><li>Exercise Prescription</li><li>Gym Based Rehab</li><li>Workplace Assessment</li><li>Ergonomics</li><li>Acupuncture</li><li>Sports Physiotherapy</li><li>Womens Health</li></ul>
  <div class="bottom"><div class="field">Referring Doctor</div><div class="field">Sign</div><div class="field">Doctors Name</div><div class="field">Address</div>
  <div class="ticks"><span>E-mail</span><span>Phone</span><span>Fax</span><span>Snail Mail</span></div></div>
</section>

<!-- business cards and magnet -->
<div class="item card wide" style="left:12px;top:192px"><div class="brand"><span class="dot"></span>Bluegate Physiotherapy</div></div>
<div class="item card wide" style="left:12px;top:213px"><div class="brand"><span class="dot"></span>Bluegate Physiotherapy</div></div>
<div class="item card orange" style="left:12px;top:242px;height:24px"><div class="brand"><span class="dot"></span>Bluegate</div></div>
<div class="item card" style="left:58px;top:242px;height:24px"><div class="brand"><span class="dot"></span>Bluegate</div></div>
<div class="item card blue" style="left:12px;top:269px;height:24px"><div class="brand"><span class="dot"></span>Bluegate</div></div>
<div class="item card green" style="left:58px;top:269px;height:24px"><div class="brand"><span class="dot"></span>Bluegate</div></div>
<div class="item card dark" style="left:12px;top:296px;height:24px"><div class="brand"><span class="dot"></span>Bluegate</div></div>
<div class="item card blue" style="left:58px;top:296px;height:24px"><div class="brand"><span class="dot"></span>Bluegate</div></div>
<div class="item card" style="left:12px;top:330px;height:20px"><div class="brand"><span class="dot"></span>Bluegate</div><div class="phone tiny">Phone 08 9535 0000</div></div>

<!-- presentation folder -->
<section class="item folder-cover">
  <div class="brand"><span class="dot"></span>Bluegate Physiotherapy</div>
  <div role="img" aria-label="Brand tree decoration in white" style="position:absolute;left:30px;top:105px;width:70px;height:60px;background:radial-gradient(circle,rgba(255,255,255,.7),transparent 65%)"></div>
  <div class="tiny" style="position:absolute;left:80px;top:140px;color:#fff;width:120px">Unit 3, 48 Kestrel Lane, Mandurah WA 6210<br>www.bluegatephysio-example.com.au</div>
</section>
<section class="item folder-inside">
  <div class="mark-area" role="img" aria-label="Faint brand tree decoration" style="left:40px;top:30px;width:110px;height:100px"></div>
  <div class="pocket"></div>
</section>

<!-- envelopes -->
<section class="item envelope" style="top:230px;height:87px">
  <div class="brand"><span class="dot"></span>Bluegate Physiotherapy</div>
  <div class="contact tiny">Unit 3, 48 Kestrel Lane, Mandurah WA 6210<br>www.bluegatephysio-example.com.au</div>
  <svg class="flap" viewBox="0 0 206 14" preserveAspectRatio="none" aria-hidden="true"><path d="M0 10 Q100 0 206 4 V14 H0Z" fill="var(--blue)"/></svg>
</section>
<section class="item envelope" style="top:322px;height:74px">
  <div class="brand"><span class="dot"></span>Bluegate Physiotherapy</div>
  <div class="contact tiny">Unit 3, 48 Kestrel Lane, Mandurah WA 6210<br>www.bluegatephysio-example.com.au</div>
  <svg class="flap" viewBox="0 0 206 14" preserveAspectRatio="none" aria-hidden="true"><path d="M0 10 Q100 0 206 4 V14 H0Z" fill="var(--orange)"/></svg>
</section>

</body>
</html>
```